professional business card

A Clean looking business card for a money transfer company. Our company is call Velorix= Transfer + Send = Transcend (next level)
to show professionalism as well as some effects to show digital tech.

1 side to have position, name and address
2 side to have company name and show that we provide money exchange and cross-border money transfer

Target Market(s)

Remittance companies and high net worth individuals

Industry/Entity Type

Finance

Contact Information for Business Card

Name, address, email, title, services- money exchange and cross-border remittance

Requirements
Nice to have
• Digital age feel

```html
<!DOCTYPE html>
<html lang="en">
<head>
<meta charset="utf-8">
<title>Velorix Business Card</title>
<link rel="stylesheet" href="https://fonts.googleapis.com/css2?family=Montserrat:wght@400;500;600&family=Figtree:wght@600;700&display=swap">
<style>
  :root {
    --navy: #263444;
    --navy-deep: #1f2b39;
    --teal: #6fcedd;
    --white: #ffffff;
    --backdrop: #c2c2c2;
  }
  * { margin: 0; padding: 0; box-sizing: border-box; }
  html, body { width: 1200px; height: 1200px; overflow: hidden; }
  body { background: var(--backdrop); position: relative; font-family: "Montserrat", sans-serif; }

  .card { position: absolute; top: 238px; width: 417px; height: 734px; overflow: hidden; }

  /* Back side */
  .card-back { left: 136px; background: var(--navy); }
  .pattern-field {
    position: absolute; inset: 0;
    background: linear-gradient(180deg, var(--navy) 0%, var(--navy-deep) 50%, var(--navy) 100%);
    opacity: 0.6;
  }
  .back-wordmark {
    position: absolute; left: 250px; top: 602px; width: 110px; text-align: center;
    font-family: "Figtree", sans-serif; font-weight: 700; font-size: 27px; color: var(--teal);
  }

  /* Front side */
  .card-front { left: 640px; background: var(--navy); text-align: center; color: var(--white); }
  .front-top { position: absolute; left: 0; top: 0; width: 100%; height: 222px; background: var(--white); }
  .company-name {
    position: absolute; left: 0; top: 44px; width: 100%;
    font-weight: 600; font-size: 55px; letter-spacing: 1px; color: var(--navy); line-height: 1;
  }
  .brand-spot {
    position: absolute; left: 50%; top: 170px; width: 104px; height: 104px; margin-left: -52px;
    border-radius: 50%; background: var(--teal); border: 10px solid var(--white);
  }
  .brand-spot-name {
    position: absolute; left: 0; top: 288px; width: 100%;
    font-family: "Figtree", sans-serif; font-weight: 700; font-size: 20px; letter-spacing: 2px; color: var(--teal);
  }
  .person-name {
    position: absolute; left: 0; top: 334px; width: 100%;
    font-family: "Figtree", sans-serif; font-weight: 700; font-size: 25px; color: var(--teal); line-height: 1.1;
  }
  .person-role { position: absolute; left: 0; top: 364px; width: 100%; font-size: 17px; line-height: 1.1; }
  .icon-row { position: absolute; left: 0; top: 406px; width: 100%; display: flex; justify-content: center; gap: 6px; }
  .icon-tile {
    width: 26px; height: 26px; border-radius: 4px; background: var(--teal);
    display: flex; align-items: center; justify-content: center;
  }
  .icon-tile svg { width: 16px; height: 16px; }
  .contact-list { position: absolute; left: 0; top: 446px; width: 100%; list-style: none; font-size: 18px; line-height: 28px; }
  .pin-tile { position: absolute; left: 50%; top: 542px; margin-left: -13px; }
  .address { position: absolute; left: 0; top: 576px; width: 100%; font-style: normal; font-size: 18px; line-height: 27px; }
  .services-band {
    position: absolute; left: 0; bottom: 0; width: 100%; height: 76px; background: var(--teal);
    display: flex; align-items: center; justify-content: center;
    font-family: "Figtree", sans-serif; font-weight: 700; font-size: 17px; line-height: 24px; color: var(--navy);
  }
</style>
</head>
<body>
  <section class="card card-back">
    <div class="pattern-field" role="img" aria-label="Embossed repeating brand-mark pattern in dark navy"></div>
    <div class="back-wordmark">Velorix</div>
  </section>

  <section class="card card-front">
    <div class="front-top"></div>
    <h1 class="company-name">VELORIX</h1>
    <div class="brand-spot"></div>
    <div class="brand-spot-name">VELORIX</div>

    <h2 class="person-name">Marcus Ellery</h2>
    <p class="person-role">Owner</p>

    <div class="icon-row">
      <span class="icon-tile">
        <svg viewBox="0 0 16 16"><path fill="#fff" d="M4.2 1.5l2 2.6-1.2 1.5c.8 1.8 2.2 3.3 4 4.3l1.5-1.2 2.6 2-1.3 2.2C7.5 12.8 3 8.3 2 3.4z"/></svg>
      </span>
      <span class="icon-tile">
        <svg viewBox="0 0 16 16"><rect x="1.5" y="3.5" width="13" height="9" rx="1" fill="#fff"/><path d="M1.8 4l6.2 4.6L14.2 4" fill="none" stroke="#6fcedd" stroke-width="1.2"/></svg>
      </span>
      <span class="icon-tile">
        <svg viewBox="0 0 16 16"><circle cx="8" cy="8" r="6.2" fill="none" stroke="#fff" stroke-width="1.4"/><path d="M1.8 8h12.4M8 1.8c-2.4 2.8-2.4 9.6 0 12.4M8 1.8c2.4 2.8 2.4 9.6 0 12.4" fill="none" stroke="#fff" stroke-width="1.1"/></svg>
      </span>
    </div>

    <ul class="contact-list">
      <li>(212) 555-0147</li>
      <li>info@velorix.com</li>
      <li>www.velorix.com</li>
    </ul>

    <span class="icon-tile pin-tile">
      <svg viewBox="0 0 16 16"><path fill="#fff" d="M8 1.5a4.5 4.5 0 0 0-4.5 4.5C3.5 9.5 8 14.5 8 14.5s4.5-5 4.5-8.5A4.5 4.5 0 0 0 8 1.5z"/><circle cx="8" cy="6" r="1.7" fill="#6fcedd"/></svg>
    </span>

    <address class="address">218 Harbor Street, 4th Floor,<br>Brookline, NY 10044</address>

    <div class="services-band"><p>Money Exchange &amp;<br>Cross-border Remittance</p></div>
  </section>
</body>
</html>
```